Aged Care Consultancy Business needs a business card design

I need a two sided business card - I want it clean and professional. Surprise me

Target Market(s)

middle aged and ageing victorians

Industry/Entity Type

Health Care

Contact Information for Business Card

Text to be included

Logo
Aged Care Consulting Services
Professional, Reliable, Affordable

Tovan Brelsick
Director
0427 31 64 92 (larger)
1300 73 29 41
tovan@wadolire.com.au
www.wadolcare.com.au
Facebook (details TBA)

include little icons beside the contact info:

- Envelope = email
- Phone = phone
- Globe = website

Font styles to use
Serif
Sans Serif

Requirements
Must have
• look proffesional and clean

```html
<!DOCTYPE html>
<html lang="en">
<head>
<meta charset="utf-8">
<title>Wadol Care – Business Card</title>
<link href="https://fonts.googleapis.com/css2?family=Fira+Sans:wght@400;500;600;700&display=swap" rel="stylesheet">
<style>
  :root {
    --page: #ecebe8;
    --card: #ffffff;
    --brand-blue: #1b4784;
    --ink: #3a3a3a;
    --accent: #e8922a;
  }
  * { margin: 0; padding: 0; box-sizing: border-box; }
  html, body {
    width: 1200px;
    height: 1200px;
    overflow: hidden;
    background: var(--page);
    font-family: "Fira Sans", sans-serif;
  }
  .canvas { position: relative; width: 1200px; height: 1200px; }
  .card {
    position: absolute;
    width: 672px;
    height: 384px;
    background: var(--card);
    box-shadow: 0 2px 6px rgba(0,0,0,0.12);
    overflow: hidden;
  }
  .card--front { left: 150px; top: 169px; }
  .card--back  { left: 340px; top: 623px; }

  .wordmark {
    color: var(--brand-blue);
    font-weight: 700;
    letter-spacing: 1px;
    line-height: 1;
    white-space: nowrap;
  }
  .card--front .wordmark {
    position: absolute;
    left: 27px;
    top: 20px;
    font-size: 86px;
  }
  .person { position: absolute; left: 30px; top: 124px; }
  .person__name {
    color: var(--brand-blue);
    font-weight: 600;
    font-size: 27px;
    letter-spacing: 0.3px;
    line-height: 32px;
  }
  .person__role {
    color: var(--ink);
    font-size: 17px;
    line-height: 22px;
    margin-top: 2px;
  }
  .contacts {
    position: absolute;
    left: 30px;
    list-style: none;
    font-size: 20px;
    color: var(--ink);
    line-height: 26px;
    white-space: nowrap;
  }
  .contacts--phone { top: 204px; }
  .contacts--online { top: 276px; }
  .contacts__label {
    display: inline-block;
    color: var(--brand-blue);
    font-weight: 600;
    min-width: 30px;
  }

  .back-brand {
    position: absolute;
    left: 0; right: 0;
    top: 222px;
    display: flex;
    align-items: center;
    justify-content: center;
    gap: 14px;
  }
  .back-brand__dot {
    width: 22px; height: 22px;
    border-radius: 50%;
    background: var(--accent);
  }
  .card--back .wordmark { font-size: 60px; }
  .back-url {
    position: absolute;
    left: 0; right: 0;
    top: 284px;
    text-align: center;
    color: var(--ink);
    font-size: 17px;
    font-weight: 500;
    letter-spacing: 5px;
    white-space: nowrap;
  }
</style>
</head>
<body>
<main class="canvas">
  <section class="card card--front" aria-label="Card front">
    <div class="wordmark">wadol care</div>
    <div class="person">
      <div class="person__name">TOVAN BRELSICK</div>
      <div class="person__role">Director</div>
    </div>
    <ul class="contacts contacts--phone">
      <li><span class="contacts__label">M</span>: 0427 31 64 92</li>
      <li><span class="contacts__label">T</span>: 1300 73 29 41</li>
    </ul>
    <ul class="contacts contacts--online">
      <li><span class="contacts__label">FB</span>: facebook address</li>
      <li><span class="contacts__label">W</span>: www.wadolcare.com.au</li>
      <li><span class="contacts__label">E</span>: tovan@wadolire.com.au</li>
    </ul>
  </section>

  <section class="card card--back" aria-label="Card back">
    <div class="back-brand">
      <span class="back-brand__dot"></span>
      <span class="wordmark">wadol care</span>
    </div>
    <div class="back-url">www.wadolcare.com.au</div>
  </section>
</main>
</body>
</html>
```